Professional digital stationary

We need a digital stationary for our brand, we already have a logo and based on that we need a design for Word, Powerpoint, mailings and Linkedin. We need to be able to re use the stationary for other things like other social media. So basically what we ask is a template for Powerpoint and Word, some e-mail headers and a nice and professional Linkedin Header.

Target Market(s)

recruitment

Font styles to use
Sans Serif

```html
<!DOCTYPE html>
<html lang="en">
<head>
<meta charset="utf-8">
<title>BrightShift – Email Header</title>
<link href="https://fonts.googleapis.com/css2?family=Montserrat:wght@300;400;500;700;800&display=swap" rel="stylesheet">
<style>
  :root {
    --green: #adcd63;
    --white: #ffffff;
    --slate: #5b5c61;
    --ink: #2f3035;
    --muted: #8a8b8f;
    --rule: #c9c9cb;
  }
  * { margin: 0; padding: 0; box-sizing: border-box; }
  html, body { width: 1200px; height: 800px; overflow: hidden; }
  body {
    position: relative;
    background: var(--white);
    font-family: "Montserrat", Arial, sans-serif;
  }
  .backdrop { position: absolute; inset: 0; }

  .header {
    position: absolute;
    left: 149px; top: 324px;
    width: 902px; height: 153px;
    background: var(--white);
    box-shadow: 0 3px 8px rgba(0,0,0,0.18);
  }
  .header__photo { position: absolute; left: 0; top: 0; }

  .brand {
    position: absolute; left: 45px; top: 30px;
    color: var(--white);
  }
  .brand__name {
    font-weight: 300; font-size: 27px; letter-spacing: 0.3px; line-height: 1;
  }
  .brand__tagline {
    font-weight: 300; font-size: 6px; margin-top: 1px; letter-spacing: 0.1px;
  }

  .headline {
    position: absolute; left: 45px; top: 82px;
    color: var(--white);
    font-weight: 300; font-size: 17px; line-height: 20px;
  }
  .headline strong { color: var(--green); font-weight: 800; font-size: 19px; }

  .badge { position: absolute; left: 423px; top: 48px; }

  .steps { position: absolute; inset: 0; }
  .step {
    position: absolute; top: 27px; width: 126px;
    text-align: center;
  }
  .step__icon { display: block; margin: 0 auto; }
  .step__title {
    margin-top: 17px;
    font-size: 7.5px; font-weight: 500; color: var(--ink);
  }
  .step__text {
    width: 100px; margin: 6px auto 0;
    font-size: 5.3px; line-height: 10.4px; color: var(--muted);
  }
  .step--signin { left: 479px; }
  .step--find   { left: 616px; }
  .step--contact{ left: 745px; }

  .divider {
    position: absolute; top: 28px; width: 1px; height: 96px;
    background: var(--rule);
  }
  .divider::after {
    content: ""; position: absolute; left: -2.5px;
    width: 6px; height: 6px; border-radius: 50%; background: var(--green);
  }
  .divider--one { left: 611px; }
  .divider--one::after { top: 83px; }
  .divider--two { left: 744px; }
  .divider--two::after { top: 7px; }
</style>
</head>
<body>
  <svg class="backdrop" width="1200" height="800" viewBox="0 0 1200 800" aria-hidden="true">
    <polygon points="770,0 1200,0 1200,800 433,800" fill="var(--green)"/>
  </svg>

  <section class="header">
    <svg class="header__photo" width="902" height="153" viewBox="0 0 902 153"
         role="img" aria-label="Photo of colleagues working together at a desk with charts, under a grey overlay">
      <defs>
        <linearGradient id="photoTone" x1="0" y1="0" x2="1" y2="1">
          <stop offset="0" stop-color="#55565b"/>
          <stop offset="0.55" stop-color="#66676c"/>
          <stop offset="1" stop-color="#4e4f54"/>
        </linearGradient>
      </defs>
      <polygon points="0,0 484,0 420,153 0,153" fill="url(#photoTone)"/>
    </svg>

    <div class="brand">
      <div class="brand__name">brightshift</div>
      <div class="brand__tagline">Great people, great fit</div>
    </div>

    <p class="headline">
      At BrightShift <strong>we like to work</strong><br>
      informally, but <strong>PROFESSIONALLY!!</strong>
    </p>

    <svg class="badge" width="56" height="56" viewBox="0 0 56 56" aria-hidden="true">
      <circle cx="28" cy="28" r="27" fill="var(--white)"/>
      <circle cx="28" cy="28" r="22" fill="var(--green)"/>
    </svg>

    <div class="steps">
      <div class="step step--signin">
        <svg class="step__icon" width="40" height="40" viewBox="0 0 40 40" aria-hidden="true">
          <circle cx="20" cy="20" r="19" fill="none" stroke="var(--green)" stroke-width="0.8"/>
          <path d="M13 15h5l1.5 2H27v10H13z" fill="none" stroke="var(--green)" stroke-width="0.9" stroke-linejoin="round"/>
          <path d="M24 22v4M22 24h4" stroke="var(--green)" stroke-width="0.9"/>
        </svg>
        <h3 class="step__title">Sign In!</h3>
        <p class="step__text">Sign up now, upload your CV and stay automatically informed of the latest assignments.</p>
      </div>

      <div class="step step--find">
        <svg class="step__icon" width="40" height="40" viewBox="0 0 40 40" aria-hidden="true">
          <circle cx="20" cy="20" r="19" fill="none" stroke="var(--green)" stroke-width="0.8"/>
          <path d="M14 23a3.5 3.5 0 0 1 1-6.8 5 5 0 0 1 9.5 0.5 3.2 3.2 0 0 1 1 6.3" fill="none" stroke="var(--green)" stroke-width="0.9"/>
          <circle cx="20" cy="21" r="2.6" fill="none" stroke="var(--green)" stroke-width="0.9"/>
          <path d="M22 23l2.5 2.5" stroke="var(--green)" stroke-width="0.9"/>
        </svg>
        <h3 class="step__title">Find your assignment</h3>
        <p class="step__text">Use our extensive search function to find the assignment that suits you.</p>
      </div>

      <div class="step step--contact">
        <svg class="step__icon" width="40" height="40" viewBox="0 0 40 40" aria-hidden="true">
          <circle cx="20" cy="20" r="19" fill="none" stroke="var(--green)" stroke-width="0.8"/>
          <circle cx="17" cy="17" r="3" fill="none" stroke="var(--green)" stroke-width="0.9"/>
          <circle cx="23.5" cy="17" r="3" fill="none" stroke="var(--green)" stroke-width="0.9"/>
          <path d="M11.5 26a5.5 5.5 0 0 1 11 0M18 26a5.5 5.5 0 0 1 11 0" fill="none" stroke="var(--green)" stroke-width="0.9"/>
        </svg>
        <h3 class="step__title">Direct contact</h3>
        <p class="step__text">Would you like to speak to us? Call email or whatapps us directly.</p>
      </div>

      <span class="divider divider--one"></span>
      <span class="divider divider--two"></span>
    </div>
  </section>
</body>
</html>
```